Safety training business card design

We need a buisness card design and logo for a small buisness that provides safety training through out the mining and civil construction industries. We provide first aid , confined space working at heights , machinery tickets, chainsaw, four wheel drive and four wheel motorbike training. We would like to use the design colors of navy blue, Fluro or lime green and white .

Industry/Entity Type

Construction

Contact Information for Business Card

Kelbrook Earthmoving & Training , Dennis Holloway, kelbrook.training@mailbox-example.com, ph 0438615044 abn 47 816 305 971

```html
<!DOCTYPE html>
<html lang="en">
<head>
<meta charset="utf-8">
<title>Kelbrook Earthmoving &amp; Training – Business Card</title>
<link rel="stylesheet" href="https://fonts.googleapis.com/css2?family=Roboto+Condensed:wght@300;400;700&display=swap">
<style>
  :root {
    --backdrop: #d2d2d2;
    --hi-vis-yellow: #fff200;
    --navy-deep: #1b1464;
    --navy: #2e3192;
    --blue: #005baa;
    --sky: #00a0e3;
    --ink-navy: #1b1464;
  }
  html, body {
    margin: 0;
    padding: 0;
    width: 1200px;
    height: 953px;
    overflow: hidden;
    background: var(--backdrop);
    font-family: "Roboto Condensed", "Arial Narrow", sans-serif;
  }
  .card {
    position: absolute;
    left: 376px;
    width: 446px;
    height: 268px;
    box-sizing: border-box;
  }
  .card-front {
    top: 173px;
    background: var(--hi-vis-yellow);
  }
  .company-name {
    position: absolute;
    left: 65px;
    top: 84px;
    margin: 0;
    color: var(--ink-navy);
    font-weight: 700;
    font-size: 31px;
    line-height: 33px;
    letter-spacing: 0.5px;
    text-transform: uppercase;
  }
  .card-back {
    top: 512px;
    background: linear-gradient(150deg,
      var(--navy-deep) 0%,
      var(--navy) 48%,
      var(--blue) 62%,
      var(--sky) 100%);
    color: var(--hi-vis-yellow);
  }
  .back-company {
    position: absolute;
    left: 82px;
    top: 66px;
    margin: 0;
    font-weight: 700;
    font-size: 9.5px;
    letter-spacing: 0.3px;
    text-transform: uppercase;
  }
  .person-name {
    position: absolute;
    left: 82px;
    top: 119px;
    margin: 0;
    font-weight: 400;
    font-size: 29px;
    line-height: 36px;
  }
  .contact {
    position: absolute;
    left: 82px;
    top: 175px;
    margin: 0;
    font-weight: 300;
    font-size: 15.5px;
    line-height: 21px;
    font-style: normal;
  }
  .contact span { display: block; }
</style>
</head>
<body>
  <section class="card card-front" aria-label="Business card front">
    <h1 class="company-name">Kelbrook<br>Earthmoving<br>&amp; Training</h1>
  </section>

  <section class="card card-back" aria-label="Business card back">
    <p class="back-company">Kelbrook Earthmoving &amp; Training</p>
    <h2 class="person-name">Dennis Holloway</h2>
    <address class="contact">
      <span class="email">kelbrook.training@mailbox-example.com</span>
      <span class="phone">ph 0438615044 abn 47 816 305 971</span>
    </address>
  </section>
</body>
</html>
```